Engineering group involved with fire safety needs a business card

We need a business card design for a company based in Greece called "Varotis Group". We are engineers and specialized technicians, operating the following : a) Fire fighting equipment trade b) Installation , Inspection & Maintenance of fire extinguishers and fire protection systems c) Occupational Health & Safety (Risk assessment & management/ Staff training). We need a clear and simple card design. I uploaded a draft I made, in order to give you an idea of the company and how I currently imagine the design of the card. I also uploaded the logo in .png file format. We are always open to different, new suggestions and ideas you may want to submit.
Target Market(s)
industries, companies, managers, retail clients
Industry/Entity Type
Fire Safety
Contact Information for Business Card
Addresses & phone numbers (headquarters + branch), logo, name (you can find all the details on the uploaded files!)
Colors
Designer to choose colors to be used in the design.
Look and feel
Each slider illustrates characteristics of the customer's brand and the style your logo design should communicate.

```html
<!DOCTYPE html>
<html lang="en">
<head>
<meta charset="utf-8">
<title>Varotis Group – Business Card</title>
<link href="https://fonts.googleapis.com/css2?family=Roboto:wght@400;500;700;900&display=swap" rel="stylesheet">
<style>
  :root {
    --brand-red: #b5121b;
    --brand-grey: #5e6366;
    --grey-dark: #4f5457;
    --grey-pattern: #676c6f;
    --text-grey: #55595c;
    --paper: #ffffff;
    --stage: #e4e5e6;
    --white: #ffffff;
  }
  * { box-sizing: border-box; margin: 0; padding: 0; }
  html, body { width: 1200px; height: 1108px; overflow: hidden; }
  body {
    background: var(--stage);
    font-family: "Roboto", Arial, sans-serif;
    position: relative;
  }
  .card {
    position: absolute;
    top: 214px;
    width: 440px;
    height: 680px;
    border-radius: 26px;
    overflow: hidden;
    box-shadow: 0 10px 30px rgba(0,0,0,0.18);
  }
  .card--front { left: 120px; background: var(--paper); }
  .card--back { left: 640px; background: var(--brand-grey); }

  /* Front */
  .brand-block {
    position: absolute; top: 96px; left: 0; right: 0;
    display: flex; flex-direction: column; align-items: center;
  }
  .brand-mark {
    width: 58px; height: 58px; background: var(--brand-red);
    margin-bottom: 18px;
  }
  .brand-name {
    font-weight: 900; font-size: 50px; letter-spacing: 1px;
    color: var(--brand-red); line-height: 1;
  }
  .brand-sub {
    font-weight: 900; font-size: 50px; letter-spacing: 4px;
    color: var(--brand-red); line-height: 1.05;
  }
  .tagline {
    display: flex; align-items: center; gap: 10px;
    margin-top: 12px;
    font-size: 13.5px; color: var(--text-grey); letter-spacing: 0.4px;
  }
  .tagline::before, .tagline::after {
    content: ""; width: 28px; height: 2px; background: var(--text-grey);
  }
  .person {
    position: absolute; top: 372px; left: 0; right: 0; text-align: center;
  }
  .person__name {
    font-weight: 700; font-size: 27px; color: var(--brand-red); letter-spacing: 0.3px;
  }
  .person__role {
    font-size: 15px; color: var(--text-grey); margin-top: 4px;
  }
  .icon-row {
    display: flex; align-items: center; justify-content: center; gap: 5px;
    margin-top: 12px;
  }
  .icon-row::before, .icon-row::after {
    content: ""; width: 52px; height: 1.5px; background: var(--text-grey); margin: 0 6px;
  }
  .icon-row svg { width: 21px; height: 21px; display: block; }
  .contact-list {
    list-style: none; margin-top: 10px;
    font-size: 15px; line-height: 21px; color: var(--text-grey);
  }
  .address {
    position: absolute; top: 598px; left: 0; right: 0; text-align: center;
    border-top: 1.5px solid var(--text-grey);
    margin: 0 110px;
  }
  .address p {
    font-size: 14.5px; line-height: 20px; color: var(--text-grey);
    white-space: nowrap; margin: 0 -110px;
  }
  .address p:first-child { margin-top: 8px; }

  /* Back */
  .back-pattern {
    position: absolute; left: 0; top: 0; width: 100%; height: 330px;
    background: linear-gradient(180deg, var(--grey-pattern) 0%, var(--brand-grey) 100%);
  }
  .back-content {
    position: absolute; top: 360px; left: 0; right: 0;
    display: flex; flex-direction: column; align-items: center; text-align: center;
  }
  .back-mark { width: 58px; height: 58px; background: var(--brand-red); margin-bottom: 16px; }
  .services {
    list-style: none;
    font-weight: 700; font-size: 16px; line-height: 23px;
    color: var(--white); letter-spacing: 0.4px; text-transform: uppercase;
  }
  .back-email { margin-top: 18px; font-size: 19px; color: var(--white); }
  .back-web { margin-top: 4px; font-size: 19px; color: var(--brand-red); }
</style>
</head>
<body>

<section class="card card--front" aria-label="Card front">
  <div class="brand-block">
    <div class="brand-mark"></div>
    <div class="brand-name">VAROTIS</div>
    <div class="brand-sub">GROUP</div>
    <div class="tagline">INSTALLATION - INSPECTION - MAINTENANCE</div>
  </div>

  <div class="person">
    <h1 class="person__name">NIKOLAOS VAROTIS</h1>
    <p class="person__role">Mechanical Engineer - OHS Consultant</p>

    <div class="icon-row" aria-hidden="true">
      <svg viewBox="0 0 22 22"><circle cx="11" cy="11" r="11" fill="#b5121b"/><path d="M6 8c0-1 1-2 2-2l1 2-1 1c1 2 2 3 4 4l1-1 2 1c0 1-1 2-2 2-4 0-7-3-7-7z" fill="#fff"/></svg>
      <svg viewBox="0 0 22 22"><circle cx="11" cy="11" r="11" fill="#b5121b"/><rect x="6" y="9" width="10" height="7" rx="1" fill="#fff"/><path d="M5 9c2-3 10-3 12 0" stroke="#fff" stroke-width="1.6" fill="none"/></svg>
      <svg viewBox="0 0 22 22"><circle cx="11" cy="11" r="11" fill="#b5121b"/><rect x="8" y="5" width="6" height="12" rx="1" fill="#fff"/></svg>
      <svg viewBox="0 0 22 22"><circle cx="11" cy="11" r="11" fill="#b5121b"/><rect x="5.5" y="7.5" width="11" height="7" fill="#fff"/><path d="M5.5 7.5l5.5 4 5.5-4" stroke="#b5121b" stroke-width="1" fill="none"/></svg>
      <svg viewBox="0 0 22 22"><circle cx="11" cy="11" r="11" fill="#b5121b"/><circle cx="11" cy="11" r="5.5" fill="none" stroke="#fff" stroke-width="1.4"/><path d="M5.5 11h11M11 5.5c-3 3-3 8 0 11M11 5.5c3 3 3 8 0 11" stroke="#fff" stroke-width="1" fill="none"/></svg>
    </div>

    <ul class="contact-list">
      <li>+30 22920 41238 (HQ)</li>
      <li>+30 210 7714529 (BO)</li>
      <li>+30 694 512 30 84</li>
      <li>www.varotisgroup.gr</li>
      <li>Nikolaos.Varotis@varotisgroup.gr</li>
    </ul>
  </div>

  <div class="address">
    <p>Headquarters: 14 Anemonis Street, 19500 Lavrio</p>
    <p>Branch Office: 22 Kiparission Lane, 15124 Marousi</p>
  </div>
</section>

<section class="card card--back" aria-label="Card back">
  <div class="back-pattern" role="img" aria-label="Faint repeating brand pattern in grey tones"></div>
  <div class="back-content">
    <div class="back-mark"></div>
    <ul class="services">
      <li>Fire Fighting Equipment</li>
      <li>Licensing &amp; Business Registration</li>
      <li>Occupational Health &amp; Safety</li>
      <li>Staff Training</li>
    </ul>
    <p class="back-email">info@varotisgroup.gr</p>
    <p class="back-web">www.varotisgroup.gr</p>
  </div>
</section>

</body>
</html>
```